Larkmoor Heritage Guild Harvest Lantern Days Event Flyer - Historic Event

I need a flyer about the Larkmoor Heritage Guild's Harvest Lantern Days event October 8th and 9th. The centerpiece of Harvest Lantern Days is Civil War reenactments. I want the flyer to include the schedule of events and be eye catching on area bulletin boards. Our website is www.larkmoorheritageguild.org for more information and pictures. The website for the Tilden Rangers reenactors is http://www.tildenrangers.com/.

Target Market(s)

Our target market is middle ages (35-70) families and couples. Most are history buffs, especially about the Civil War.

Industry/Entity Type

Non-Profit

Font styles to use
Serif
Decorative
Script

Requirements
Must have
• The flyer must include the majority of the schedule attached - especially the battle times, museums, and anything including food.The dance on Saturday night is also important. The bottom of the flyer MUST say "Paid in part by Osgood County Visitor Fund Board"
Nice to have
• Pictures

```html
<!DOCTYPE html>
<html lang="en">
<head>
<meta charset="utf-8">
<title>Larkmoor Heritage Guild – Harvest Lantern Days</title>
<link rel="stylesheet" href="https://fonts.googleapis.com/css2?family=Rye&family=Sancreek&family=Crimson+Text:wght@400;600;700&display=swap">
<style>
  :root {
    --ember: #b8360c;
    --ember-deep: #6e1a04;
    --char: #2e0a02;
    --maroon: #5c1208;
    --ink: #3a0904;
    --band: #5a1107;
    --band-text: #f6b43a;
    --cell-text: #f3d7a6;
    --photo-wood: #7a4a26;
    --photo-canvas: #d9cdb0;
  }
  * { box-sizing: border-box; margin: 0; padding: 0; }
  html, body { width: 816px; height: 1200px; overflow: hidden; }
  body {
    position: relative;
    background: radial-gradient(ellipse at 50% 50%, #e0621a 0%, var(--ember) 55%, var(--ember-deep) 100%);
    font-family: "Crimson Text", Georgia, serif;
    color: var(--ink);
  }
  .paper { position: absolute; inset: 0; }
  .flyer { position: absolute; inset: 0; }

  .title {
    position: absolute; left: 0; width: 816px; text-align: center;
    font-family: "Rye", serif; color: var(--maroon); line-height: 1; white-space: nowrap;
  }
  .title-main { top: 84px; font-size: 114px; }
  .title-sub { top: 214px; font-size: 60px; }

  .event-banner {
    position: absolute; left: 86px; top: 292px; width: 644px; height: 64px;
    background: var(--band);
    clip-path: polygon(4% 0, 96% 0, 100% 50%, 96% 100%, 4% 100%, 0 50%);
    display: flex; align-items: center; justify-content: center;
    font-family: "Sancreek", serif; font-size: 36px; letter-spacing: 2px;
    color: var(--band-text); text-transform: uppercase; white-space: nowrap;
  }
  .flourish {
    position: absolute; left: 364px; top: 366px; width: 88px; height: 12px;
    background: var(--maroon); border-radius: 6px; opacity: .85;
  }

  .day-band {
    position: absolute; left: 72px; width: 672px; height: 40px;
    background: var(--band);
    display: flex; align-items: center; justify-content: center;
    font-family: "Rye", serif; font-size: 26px; letter-spacing: 6px;
    color: var(--band-text); text-transform: uppercase; word-spacing: 16px; white-space: nowrap;
  }
  .day-band.saturday { top: 408px; }
  .day-band.sunday { top: 822px; }

  .day-note {
    position: absolute; left: 60px; top: 452px; width: 696px; text-align: center;
    font-size: 20px; font-weight: 700; color: var(--maroon); white-space: nowrap;
  }

  .schedule-sat { position: absolute; left: 67px; top: 486px; width: 700px; }
  .schedule-sat::before {
    content: ""; position: absolute; left: 0; top: 0; width: 122px; height: 318px;
    background: var(--band);
  }
  .row { position: relative; display: flex; height: 29px; align-items: center; white-space: nowrap; }
  .row .time { width: 122px; padding-left: 8px; font-size: 18px; font-weight: 600; color: var(--cell-text); }
  .row .what { padding-left: 12px; font-size: 20px; font-weight: 700; color: var(--ink); }
  .row .what.note { font-weight: 400; font-size: 18px; }

  .schedule-sun { position: absolute; left: 110px; top: 872px; width: 428px; }
  .schedule-sun::before {
    content: ""; position: absolute; right: 0; top: 0; width: 108px; height: 210px;
    background: var(--band);
  }
  .row-sun { position: relative; display: flex; height: 30px; align-items: center; white-space: nowrap; }
  .row-sun .what { width: 320px; text-align: right; padding-right: 12px; font-size: 20px; font-weight: 700; color: var(--maroon); }
  .row-sun .what.note { font-weight: 400; font-size: 18px; }
  .row-sun .time { width: 108px; padding-left: 10px; font-size: 18px; font-weight: 600; color: var(--cell-text); }

  .camp-photo {
    position: absolute; left: 542px; top: 872px; width: 200px; height: 210px;
    background: linear-gradient(180deg, #e8e2cf 0%, var(--photo-canvas) 35%, var(--photo-wood) 70%, #4b2c16 100%);
    border: 2px solid var(--char);
  }

  .footer {
    position: absolute; left: 72px; top: 1094px; width: 672px; text-align: center;
    color: var(--maroon); line-height: 1.25; white-space: nowrap;
  }
  .footer .sites { font-size: 17px; font-weight: 600; }
  .footer .funding { font-size: 18px; font-weight: 700; }
</style>
</head>
<body>
  <svg class="paper" width="816" height="1200" viewBox="0 0 816 1200" aria-hidden="true">
    <defs>
      <radialGradient id="parchmentGlow" cx="50%" cy="45%" r="65%">
        <stop offset="0%" stop-color="#fbe06a"/>
        <stop offset="55%" stop-color="#f7c233"/>
        <stop offset="85%" stop-color="#ec8d1c"/>
        <stop offset="100%" stop-color="#c9520c"/>
      </radialGradient>
      <filter id="scorch" x="-5%" y="-5%" width="110%" height="110%">
        <feGaussianBlur stdDeviation="6"/>
      </filter>
      <path id="paperEdge" d="M58 34 L130 22 L210 40 L300 18 L390 30 L470 14 L560 32 L650 20 L730 36 L790 24 L782 120 L798 220 L776 330 L792 450 L780 560 L796 680 L774 800 L792 920 L778 1040 L790 1176 L700 1166 L610 1184 L520 1168 L420 1186 L330 1170 L230 1188 L140 1172 L40 1182 L54 1060 L30 940 L50 820 L28 700 L48 580 L26 460 L46 340 L24 220 L44 110 Z"/>
    </defs>
    <use href="#paperEdge" fill="url(#parchmentGlow)"/>
    <use href="#paperEdge" fill="none" stroke="#8a2a05" stroke-width="18" filter="url(#scorch)"/>
    <use href="#paperEdge" fill="none" stroke="#2e0a02" stroke-width="5"/>
  </svg>

  <main class="flyer">
    <h1 class="title title-main">Larkmoor</h1>
    <div class="title title-sub">Heritage Guild's</div>
    <div class="event-banner">Harvest Lantern Days Event</div>
    <div class="flourish" role="img" aria-label="Decorative flourish"></div>

    <div class="day-band saturday">Saturday October 8th 2016</div>
    <p class="day-note">Through the Day – Demonstrations and Speakers in various locations</p>

    <section class="schedule-sat">
      <div class="row"><span class="time">10:00 AM</span><span class="what">Battle by Tilden Rangers</span></div>
      <div class="row"><span class="time"></span><span class="what note">- Sponsored in part by Hollis General Stores</span></div>
      <div class="row"><span class="time">11:30-1:00</span><span class="what">Chicken Biscuit Bake at Town Hall – Free Will Donation</span></div>
      <div class="row"><span class="time">Afternoon</span><span class="what note">Trolley and Buggy Rides</span></div>
      <div class="row"><span class="time">1:00-4:00</span><span class="what">Museums Opens</span></div>
      <div class="row"><span class="time">1:30-2:00</span><span class="what">Birthday Cake on Merritt House Front Porch</span></div>
      <div class="row"><span class="time"></span><span class="what note">- Cake donated by Pennick Grocers - Avon City</span></div>
      <div class="row"><span class="time">2:00</span><span class="what">Battle by Tilden Rangers</span></div>
      <div class="row"><span class="time">3:00</span><span class="what">Sightseeing Cruise on the Spirit of Larkmoor</span></div>
      <div class="row"><span class="time">6:00</span><span class="what">Dance at Town Hall with Cedar Hollow Band</span></div>
      <div class="row"><span class="time"></span><span class="what note">- Sponsored by Dr. Wenley</span></div>
    </section>

    <div class="day-band sunday">Sunday October 9th 2016</div>

    <section class="schedule-sun">
      <div class="row-sun"><span class="what">PM Parade on Main Street</span><span class="time">12:30 PM</span></div>
      <div class="row-sun"><span class="what note">- Buggy &amp; Trolley Rides</span><span class="time">Afternoon</span></div>
      <div class="row-sun"><span class="what">Museums Open</span><span class="time">1:00-4:00</span></div>
      <div class="row-sun"><span class="what">Battle by Tilden Rangers</span><span class="time">1:30</span></div>
      <div class="row-sun"><span class="what">Pie Reception at Larkmoor Depot</span><span class="time">2:00</span></div>
      <div class="row-sun"><span class="what">and Railroad History Museum</span><span class="time"></span></div>
      <div class="row-sun"><span class="what">Sightseeing Cruise</span><span class="time">3:00</span></div>
    </section>

    <div class="camp-photo" role="img" aria-label="Photo of a canvas-covered wooden wagon at a historic encampment"></div>

    <footer class="footer">
      <p class="sites">www.larkmoorheritageguild.org &nbsp;·&nbsp; http://www.tildenrangers.com/</p>
      <p class="funding">Paid in part by Osgood County Visitor Fund Board</p>
    </footer>
  </main>
</body>
</html>
```